Real Estate - Real Estate
Real Estate
Real Estate Company Arrange auction for land selling Real Estate services
- No scrolling - page fit to screen - You need to pick a good arabic font with good colour "If you don't know arabic keep as in photoshop". - This company have no Identity and color theme, its for you to decide - Social media links needed - Arabic interface (Right to left arrangement) - Boss photo attached need to be in the home page. - Welcome message from boss. - Section in the home page for auction announcement "lands auction". - You need to read photoshop layer name to understand the arabic name. - You decide Font colour and type the colour in the photoshop is just for showing. - No field to take any data in the home page.
kiromeltub kiromeltub
Consider it as official website
Graphics - architectural drawings
Please ignore uploaded picture
Please don't focus in Jeddah. Instead focus on "Real Estate" and add some graphics.
I uploaded some picture for jeddah please check it.
This website about jeddah - saudi arabia city only, I will upload some related photo which could be better to use, you pick what you think is better or check with google images.

```html
<!DOCTYPE html>
<html lang="ar" dir="rtl">
<head>
<meta charset="utf-8">
<title>دار المزاد العقاري</title>
<link rel="stylesheet" href="https://fonts.googleapis.com/css2?family=Aref+Ruqaa:wght@400;700&family=Great+Vibes&family=Arimo:wght@400&display=swap">
<style>
  :root {
    --nav-bg: #1c1d3a;
    --nav-text: #c9cbe6;
    --sky-top: #3a3f8a;
    --sky-mid: #6f73c4;
    --sky-low: #a9a3d6;
    --pattern: #2b3ca8;
    --band: rgba(22, 24, 60, 0.86);
    --band-edge: #14163a;
    --footer: #0e0f28;
    --white: #ffffff;
    --muted: #d9dbf2;
    --accent: #f29a1a;
    --brace: #e8e9f7;
    --social: #3d6fc4;
  }
  * { margin: 0; padding: 0; box-sizing: border-box; }
  html, body { width: 1200px; height: 665px; overflow: hidden; background: var(--footer); }
  .page { position: relative; width: 1200px; height: 665px; overflow: hidden; direction: ltr; }

  .hero-scene {
    position: absolute; inset: 0;
    background:
      radial-gradient(ellipse 420px 200px at 470px 360px, rgba(220,200,235,0.55), transparent 70%),
      linear-gradient(180deg, var(--sky-top) 0%, var(--sky-mid) 42%, var(--sky-low) 62%, #6a5e8e 78%, #2b2a52 100%);
  }
  .corner-pattern { position: absolute; }
  .corner-pattern.left {
    left: 0; top: 0; width: 300px; height: 470px;
    background: linear-gradient(135deg, var(--pattern) 0%, rgba(43,60,168,0.35) 70%, transparent 100%);
  }
  .corner-pattern.right {
    right: 0; top: 0; width: 260px; height: 460px;
    background: linear-gradient(225deg, var(--pattern) 0%, rgba(43,60,168,0.35) 70%, transparent 100%);
  }

  .main-nav {
    position: absolute; top: 0; left: 0; width: 1200px; height: 34px;
    background: var(--nav-bg);
    display: flex; gap: 58px; padding-left: 70px; align-items: center;
    font-family: "Great Vibes", cursive; font-size: 25px; color: var(--nav-text);
  }
  .main-nav .active { color: var(--white); }

  .site-title {
    position: absolute; top: 58px; left: 360px; width: 700px;
    font-family: "Aref Ruqaa", serif; font-weight: 700; font-size: 96px;
    color: var(--white); text-align: center; direction: rtl; line-height: 1.2;
    text-shadow: 0 2px 8px rgba(20,20,70,0.5);
  }

  .welcome-name {
    position: absolute; right: 365px; top: 232px; direction: rtl;
    font-family: "Aref Ruqaa", serif; font-size: 34px; color: var(--white);
  }
  .welcome-role {
    position: absolute; right: 365px; top: 285px; direction: rtl;
    font-family: "Aref Ruqaa", serif; font-size: 38px; color: var(--white);
  }
  .chair-photo {
    position: absolute; left: 845px; top: 180px; width: 206px; height: 240px;
    border: 6px solid #eef0fb;
    background: linear-gradient(180deg, #c9d4e4 0%, #e9edf3 55%, #f5f5f5 100%);
  }

  .auction-band {
    position: absolute; left: 0; top: 451px; width: 1200px; height: 178px;
    background: var(--band);
    clip-path: polygon(120px 0, 1200px 0, 1200px 178px, 0 178px, 0 120px);
  }
  .auction-band::before {
    content: ""; position: absolute; left: 0; top: 0; width: 250px; height: 178px;
    background: linear-gradient(90deg, var(--band-edge), transparent);
  }
  .event-date {
    position: absolute; left: 255px; top: 468px; width: 190px; text-align: center;
    font-family: "Great Vibes", cursive; color: var(--white);
  }
  .event-date .day-label { font-size: 24px; display: block; }
  .event-date .day-count { font-size: 46px; line-height: 1.1; display: block; }
  .event-date .day-count small { font-size: 28px; }
  .event-date .register { font-size: 30px; color: var(--accent); display: block; margin-top: 2px; }

  .auction-summary {
    position: absolute; left: 420px; top: 472px; width: 278px;
    font-family: "Arimo", sans-serif; font-size: 14.5px; line-height: 1.33;
    color: var(--muted); direction: ltr;
  }
  .auction-photo {
    position: absolute; left: 713px; top: 473px; width: 122px; height: 132px;
    border: 3px solid #eef0fb;
    background: linear-gradient(160deg, #9cc3e8 0%, #4a84bd 50%, #1f4f85 100%);
  }
  .auction-brace { position: absolute; left: 848px; top: 470px; }
  .auction-title {
    position: absolute; left: 885px; top: 512px;
    font-family: "Great Vibes", cursive; font-size: 40px; color: var(--white);
  }

  .site-footer {
    position: absolute; left: 0; top: 629px; width: 1200px; height: 36px;
    background: var(--footer);
    display: flex; align-items: center;
    font-family: "Arimo", sans-serif; font-size: 13px; color: var(--muted);
  }
  .site-footer .copyright { position: absolute; left: 750px; }
  .social-links { position: absolute; left: 945px; display: flex; gap: 20px; }
  .social-links span { width: 24px; height: 24px; border-radius: 4px; background: var(--social); display: block; }
</style>
</head>
<body>
<div class="page">
  <div class="hero-scene" role="img" aria-label="Evening view of a waterfront mosque with a domed roof under a violet sky"></div>
  <div class="corner-pattern left" role="img" aria-label="Blue interlaced geometric ornament"></div>
  <div class="corner-pattern right" role="img" aria-label="Blue interlaced geometric ornament"></div>

  <nav class="main-nav">
    <span>Auction Valuation</span>
    <span>Selling at Auction</span>
    <span>Buying at Auction</span>
    <span>About</span>
    <span class="active">Home</span>
  </nav>

  <h1 class="site-title">دار المزاد العقاري</h1>

  <p class="welcome-name">سامر بن فيصل الحربي</p>
  <p class="welcome-role">رئيس دار المزاد العقاري</p>
  <div class="chair-photo" role="img" aria-label="Portrait photo of the chairman"></div>

  <section class="auction-band" aria-label="Lands auction"></section>
  <div class="event-date">
    <span class="day-label">Sep 10, 2014</span>
    <span class="day-count">5<small>Day</small></span>
    <span class="register">Register Now</span>
  </div>
  <p class="auction-summary">Lorem ipsum dolor sit amet, consectetur adipiscing elit. Vestibulum mattis porttitor nulla, eget eleifend metus gravida id. Nunc sollicitudin nunc at tellus pretium a pulvinar purus elementum.</p>
  <div class="auction-photo" role="img" aria-label="Photo of a modern glass office tower"></div>
  <svg class="auction-brace" width="28" height="140" viewBox="0 0 28 140" aria-hidden="true">
    <path d="M4 3 Q14 3 14 16 L14 56 Q14 68 24 70 Q14 72 14 84 L14 124 Q14 137 4 137" fill="none" stroke="var(--brace)" stroke-width="3"/>
  </svg>
  <h2 class="auction-title">Lands Auction</h2>

  <footer class="site-footer">
    <span class="copyright">Copyright 2014. All right reserved.</span>
    <div class="social-links">
      <span aria-label="Social link one"></span>
      <span aria-label="Social link two"></span>
      <span aria-label="Social link three"></span>
    </div>
  </footer>
</div>
</body>
</html>
```